Commercial Real Estate

We need a business card design for a new commercial real estate business that specializes in apartment building brokerage. Not individual units but the entire complex. We find and represent the owners existing buildings and well as new buyers for those buildings. The design should convey trust, integrity, knowledge and growth. It should be easily read.

Target Market(s)

40 to 65 years old

Industry/Entity Type

Real Estate

```html
<!DOCTYPE html>
<html lang="en">
<head>
<meta charset="utf-8">
<title>Brightrow Property Investments – Business Card</title>
<link href="https://fonts.googleapis.com/css2?family=Open+Sans:wght@400;600&display=swap" rel="stylesheet">
<style>
  :root {
    --backdrop: #2a2a2c;
    --card: #f3f3f5;
    --teal: #4fb3ad;
    --slate: #4f6664;
    --facade-light: #eef2c8;
    --facade-mid: #d6ead3;
    --facade-cool: #cfe6e3;
  }
  html, body {
    margin: 0;
    width: 1200px;
    height: 1000px;
    overflow: hidden;
    background: var(--backdrop);
    font-family: "Open Sans", sans-serif;
  }
  .card {
    position: absolute;
    left: 100px;
    top: 200px;
    width: 1000px;
    height: 600px;
    background: var(--card);
    overflow: hidden;
    box-shadow: 0 10px 30px rgba(0,0,0,.45);
  }
  .card__art {
    position: absolute;
    inset: 0;
  }
  .brand {
    position: absolute;
    left: 440px;
    top: 80px;
    display: flex;
    align-items: center;
    gap: 18px;
  }
  .brand__mark {
    width: 34px;
    height: 34px;
    background: var(--teal);
  }
  .brand__name {
    font-size: 64px;
    font-weight: 600;
    color: var(--slate);
    letter-spacing: 2px;
    line-height: 1;
  }
  .brand__tagline {
    position: absolute;
    left: 492px;
    top: 166px;
    width: 360px;
    padding-top: 8px;
    border-top: 3px solid var(--teal);
    font-size: 20px;
    font-weight: 600;
    letter-spacing: 4px;
    color: var(--slate);
  }
  .card__title {
    position: absolute;
    left: 560px;
    top: 280px;
    margin: 0;
    font-size: 38px;
    font-weight: 400;
    color: var(--teal);
  }
  .contact {
    position: absolute;
    left: 690px;
    top: 420px;
    margin: 0;
    padding: 0;
    list-style: none;
  }
  .contact__item {
    display: flex;
    align-items: center;
    gap: 12px;
    height: 44px;
    font-size: 23px;
    color: var(--teal);
  }
  .contact__icon {
    width: 24px;
    height: 24px;
    flex: none;
  }
</style>
</head>
<body>
  <div class="card">
    <svg class="card__art" width="1000" height="600" viewBox="0 0 1000 600">
      <defs>
        <linearGradient id="facadeTone" x1="0" y1="0" x2="1" y2="1">
          <stop offset="0" stop-color="var(--facade-mid)"/>
          <stop offset="0.5" stop-color="var(--facade-light)"/>
          <stop offset="1" stop-color="var(--facade-cool)"/>
        </linearGradient>
      </defs>
      <polygon role="img" aria-label="Perspective view of a tall apartment building facade"
               points="0,0 175,0 620,600 0,600" fill="url(#facadeTone)"/>
      <line class="edge-line" x1="180" y1="0" x2="628" y2="600" stroke="var(--teal)" stroke-width="5"/>
    </svg>

    <div class="brand">
      <span class="brand__mark"></span>
      <span class="brand__name">Brightrow</span>
    </div>
    <div class="brand__tagline">Property Investments</div>

    <h1 class="card__title">Brightrow Buildings</h1>

    <ul class="contact">
      <li class="contact__item">
        <svg class="contact__icon" viewBox="0 0 24 24"><rect x="7" y="2" width="10" height="20" rx="2" fill="var(--slate)"/><rect x="9" y="5" width="6" height="6" fill="var(--card)"/></svg>
        0000035,004100
      </li>
      <li class="contact__item">
        <svg class="contact__icon" viewBox="0 0 24 24" fill="none" stroke="var(--slate)" stroke-width="2"><circle cx="12" cy="12" r="9"/><ellipse cx="12" cy="12" rx="4" ry="9"/><line x1="3" y1="12" x2="21" y2="12"/></svg>
        www.brightrow.com
      </li>
      <li class="contact__item">
        <svg class="contact__icon" viewBox="0 0 24 24" fill="none" stroke="var(--slate)" stroke-width="2"><rect x="2" y="5" width="20" height="14"/><polyline points="2,5 12,13 22,5"/></svg>
        hello@brightrow.net
      </li>
    </ul>
  </div>
</body>
</html>
```